Surgical Procedure Room Letterhead

PLEASE DO NOT MAKE YOUR LETTERHEAD SIMILAR TO THE ONE I AM INCLUDING IN MY UPLOADS

Hello! I need my logo used to make a very clean, professional, simple letterhead that has all the pertinent information in it:
Location: 4182 NW 38th Lane, Suite 500
Tamarac, FL 33967
Phone: 954-218-4650
Fax: 800-642-9082

Can you please put this all on a word document that is easily editable? I will include my practice letterhead as an example ONLY of how easy it should be to write below the letterhead. Please don't make this letterhead the same as the one I am including in this example. They are two separate businesses.

Target Market(s)

Insurance companies

Industry/Entity Type

medical

Requirements
Must have
• classiness, elegance, simplicity
Should not have
• Please don't make your letterhead the same as the one that I included in my uploads

```html
<!DOCTYPE html>
<html lang="en">
<head>
<meta charset="utf-8">
<title>Calloway Surgical Suites – Letterhead</title>
<link rel="stylesheet" href="https://fonts.googleapis.com/css2?family=Arimo:wght@400;700&family=Mulish:wght@700&family=PT+Sans+Narrow&display=swap">
<style>
  :root {
    --backdrop: #cccccc;
    --paper: #ffffff;
    --navy: #0f2d5a;
    --gold: #d4ad3c;
    --ink: #555555;
    --rule: #777777;
  }
  html, body {
    margin: 0;
    width: 1023px;
    height: 1200px;
    overflow: hidden;
    background: var(--backdrop);
  }
  .sheet {
    position: absolute;
    left: 180px;
    top: 130px;
    width: 663px;
    height: 940px;
    background: var(--paper);
    box-shadow: 2px 2px 4px rgba(0,0,0,0.35);
    color: var(--ink);
  }
  .brand {
    position: absolute;
    left: 36px;
    top: 62px;
  }
  .brand-name {
    font-family: "Arimo", sans-serif;
    font-weight: 700;
    font-size: 21px;
    line-height: 24px;
    color: var(--navy);
    white-space: nowrap;
  }
  .contact {
    position: absolute;
    left: 468px;
    top: 46px;
    padding-left: 8px;
    border-left: 1px solid var(--rule);
    font-family: "Arimo", sans-serif;
    font-size: 11px;
    line-height: 13.5px;
  }
  .contact-line { display: flex; align-items: center; gap: 4px; white-space: nowrap; }
  .contact-line svg { width: 9px; height: 9px; }
  .address { margin-top: 5px; white-space: nowrap; }
  .salutation {
    position: absolute;
    left: 60px;
    top: 288px;
    margin: 0;
    font-family: "Mulish", sans-serif;
    font-weight: 700;
    font-size: 15px;
  }
  .body-copy {
    position: absolute;
    left: 59px;
    top: 333px;
    width: 560px;
    font-family: "Arimo", sans-serif;
    font-size: 10.8px;
    line-height: 13.7px;
  }
  .body-copy p { margin: 0 0 12px; white-space: nowrap; }
  .closing {
    position: absolute;
    left: 60px;
    top: 614px;
    font-family: "Mulish", sans-serif;
    font-weight: 700;
    font-size: 8.5px;
  }
  .signature {
    position: absolute;
    left: 76px;
    top: 659px;
    font-family: "PT Sans Narrow", sans-serif;
    font-size: 17px;
    letter-spacing: -0.8px;
  }
</style>
</head>
<body>
<div class="sheet">
  <header>
    <div class="brand">
      <span class="brand-name">Calloway Surgical Suites</span>
    </div>
    <div class="contact">
      <div class="contact-line">
        <svg viewBox="0 0 10 10"><path d="M2 1l2 2-1 1.2c.6 1.2 1.5 2.1 2.8 2.8L7 6l2 2-1.3 1.3C4.5 9 1 5.5.7 2.3z" fill="var(--gold)"/></svg>
        954-218-4650
      </div>
      <div class="contact-line">
        <svg viewBox="0 0 10 10"><rect x="2.5" y="1" width="5" height="3" fill="var(--gold)"/><rect x="0.5" y="4" width="9" height="4.5" rx="1" fill="var(--gold)"/></svg>
        800-642-9082
      </div>
      <div class="address">4182 NW 38th Lane, Suite 500<br>Tamarac, FL 33967</div>
    </div>
  </header>

  <h1 class="salutation">Dear Mr. Smith,</h1>

  <div class="body-copy">
    <p>Lorem ipsum dolor sit amet, consectetuer adipiscing elit, sed diam nonmmy nibh euismod tincidunt ut laor<br>eet dolore magna aliquam erat volutpat. Ut wisi enim ad minim veniam, quis nostrud exerci tationmcorper<br>suscipit lobortis nisl ut aliquip ex ea commodo consequat. Duis autem vel eum iriure dolor in hendrerit in<br>vulputate velit esse molestie consequat, vel illum dolore eu feugiat</p>
    <p>Rorem ipsum dolor sit amet, consectetuer adipiscing elit, sed diam nonmmy nibh euismod tincidunt ut laor<br>eet dolore magna aliquam erat volutpat. Ut wisi enim ad minim veniam, quis nostrud exerci tationmcorper<br>suscipit lobortis nisl ut aliquip ex ea commodo consequat. Duis autem vel eum iriure dolor in hendrerit in<br>vulputate velit esse molest</p>
    <p>Dorem ipsum dolor sit amet, consectetuer adipiscing elit, sed diam nonmmy nibh euismod tincidunt ut laor<br>eet dolore magna aliquam erat volutpat. Ut wisi enim ad minim veniam, quis nostrud exerci tationmcorper<br>suscipit lobortis nisl ut aliquip ex ea commodo consequat. Duis autem vel eum iriure dolor in hendrerit in<br>suscipit lobortis nisl ut aliquip ex ea commodo consequat. Duis autem vel eum iriure dolor in hendrerit in<br>vulputate velit esse molestie consequat, vel illum</p>
    <p>Sorem ipsum dolor sit amet, consectetuer adipiscing elit, sed diam nonmmy nibh euismod tincidunt ut laor<br>eet dolore magna aliquam erat volutpat. Ut wisi enim ad minim veniam, quis nostrud exerci tationmcorper<br>suscipit lobortis nisl ut aliquip ex ea commodo consequat. Duis autem vel eum iriure dolor in</p>
  </div>

  <div class="closing">Sincerely,</div>
  <div class="signature">Daniel k Marsh</div>
</div>
</body>
</html>
```